弊社で製造・販売しているお酢のラベルデザインをお願いします。

商品は純りんご酢にはちみつを合わせた物で、4倍程度に希釈して健康飲料として利用してもらう物です。(料理にも使えます)

以前よりこの商品は500ml入りとして販売していましたが、昨今の原料費高騰等を受け、
容量を300mlに変更する事にしました。
瓶も、角瓶だったものを丸瓶に変更します。
ご愛顧いただいていたお客様に、なるべく「これまでのがすごく小さく(少なく)なってしまった・・・」という印象をもたれないように、全く新しいイメージのラベルデザインにしたいと考えています。

価格は1300円程度です。
お酢としては高額の商品ですので、「高級感」のあるデザインを希望します。

さらに、購入者のほとんどが女性ですので、女性が手に取りたくなるような
「かわいらしさ」あるいは「オシャレ感」、「健康」をイメージさせるデザインを希望します。

もちろん、スーパーや百貨店の売り場に並んだ際、他社の商品に埋もれない
目を引くデザインであってほしいと思います。

ラベルサイズは縦90mm×横145mm
瓶に巻いた際に正面に見える部分は、おおよそ90mm×73mm になります。

商品名は「やまぶき畑のしずく」
商品名以外に正面に見える部分に入れてほしい文言は以下の3つです。

「4倍濃縮タイプ」「国内産りんご果汁使用」「あなたの元気を応援!」

写真ファイルを添付しますが、
新しい瓶は丸型で色は緑。キャップはゴールドです。

これまでの商品写真も添付致します。
イメージの全く違うものを希望します。

今回は、既存の商品の容量を小さくするにあたり、これまでとは違う雰囲気である事を最大のポイントとしました。

当選ラベルは、これまでの「かわいらしい」イメージから、大人っぽさ、清楚で上品な雰囲気を感じさせ好感を得ました。
またりんご型の白地に商品名が映え、目を引きました。白地の面積は修正により、正面からりんご型がより見えるようにしました。
ピンクのバックは赤やゴールド系のデザインが多かった中で、一際優しさを感じさせ、
女性が手に取りたくなる商品だと思います。

以上の理由により選ばせていただきました。

この度は、弊社商品のラベルデザインに多くの提案をいただき、ありがとうございました。

「りんご」と「はちみつ」という、よくある組み合わせでしたが、
どのデザインもそれぞれによく練られており選定には大変時間を要しました。

今回はご縁がなかった皆様におかれましても、
またの機会がありましたら、是非もう一度お力をお貸しいただければと思います。
本来であればお一人お一人にお礼を申し上げるべきですのに、
このコメントをもってお礼に代えさせていただきます事、どうぞご容赦ください。

ご応募、本当にありがとうございました。

```html
<!DOCTYPE html>
<html lang="ja">
<head>
<meta charset="utf-8">
<title>やまぶき畑のしずく ラベル</title>
<link rel="stylesheet" href="https://fonts.googleapis.com/css2?family=Klee+One:wght@600&family=Noto+Sans+JP:wght@400;700&display=swap">
<style>
  :root {
    --page: #f4f4f2;
    --label-bg: #241816;
    --title-gold: #eba63c;
    --badge-yellow: #f3d44c;
    --badge-glow: #fff3b8;
    --ink: #1a1210;
    --white: #ffffff;
    --apple-red: #c8202a;
  }
  html, body {
    margin: 0;
    width: 836px;
    height: 1200px;
    overflow: hidden;
    background: var(--page);
  }
  .label {
    position: absolute;
    left: 68px;
    top: 131px;
    width: 700px;
    height: 937px;
    background: var(--label-bg);
    overflow: hidden;
    font-family: "Noto Sans JP", sans-serif;
  }
  .tagline {
    position: absolute;
    top: 44px;
    left: 0;
    width: 100%;
    text-align: center;
    color: var(--white);
    font-size: 42px;
    letter-spacing: 1px;
    margin: 0;
  }
  .product-name {
    position: absolute;
    margin: 0;
    writing-mode: vertical-rl;
    font-family: "Klee One", cursive;
    font-weight: 600;
    color: var(--title-gold);
    font-size: 76px;
    line-height: 1;
    letter-spacing: 6px;
  }
  .product-name--first { left: 408px; top: 112px; }
  .product-name--second { left: 280px; top: 370px; }
  .origin-badge {
    position: absolute;
    left: 596px;
    top: 113px;
    width: 88px;
    height: 463px;
    border-radius: 44px;
    background: var(--badge-yellow);
    box-shadow: 0 0 8px 3px var(--badge-glow);
    display: flex;
    align-items: center;
    justify-content: center;
  }
  .origin-badge span {
    writing-mode: vertical-rl;
    color: var(--ink);
    font-weight: 700;
    font-size: 38px;
    letter-spacing: 3px;
  }
  .concentrate {
    position: absolute;
    left: 100px;
    top: 417px;
    margin: 0;
    writing-mode: vertical-rl;
    color: var(--white);
    font-size: 46px;
    letter-spacing: 9px;
  }
  .apple-art {
    position: absolute;
    left: 139px;
    top: 795px;
    width: 424px;
    height: 142px;
  }
</style>
</head>
<body>
  <main class="label">
    <p class="tagline">あなたの元気を応援！</p>
    <h1 class="product-name product-name--first">やまぶき畑の</h1>
    <p class="product-name product-name--second">しずく</p>
    <div class="origin-badge"><span>国内産りんご果汁使用</span></div>
    <p class="concentrate">４倍濃縮タイプ</p>
    <svg class="apple-art" role="img" aria-label="りんごのイラスト（赤いりんごの上半分と茶色の軸）" viewBox="0 0 424 142">
      <rect x="0" y="62" width="424" height="80" rx="40" fill="var(--apple-red)"/>
    </svg>
  </main>
</body>
</html>
```